Luma Harbor Vow Studio, Inc.

Luma Harbor Vow Studio Business Card design for Cardlyne. Clean, contemporary, creative, colorful (using colors provided). ONE SIDE SHOULD INCLUDE logo, www.lumaharborvowstudio.com, @sayidoatluma. OTHER SIDE SHOULD INCLUDE Delia Brennan. Owner & Officiant. Isabela, Puerto Rico. 555.014.2871. delia@lumaharborvowstudio.com. Colors are blue #58AA9E
and golden #e2bf80)

Target Market(s)

Destination Wedding Clients in the United States

Contact Information for Business Card

Delia Brennan
Owner & Officiant
Isabela, Puerto Rico
555.014.2871
delia@lumaharborvowstudio.com

Font styles to use
Sans Serif

Requirements
Must have
• Colorful (colors are blue #58AA9E
• and golden #e2bf80), clean, contemporary. ONE SIDE SHOULD INCLUDE logo, www.lumaharborvowstudio.com, @sayidoatluma. Other side should include Delia Brennan. Owner & Officiant. Isabela, Puerto Rico. 555.014.2871. delia@lumaharborvowstudio.com
Nice to have
• I would like to see a version that includes my bio photo, and one that doesn't include the bio photo

```html
<!DOCTYPE html>
<html lang="en">
<head>
<meta charset="utf-8">
<title>Luma Harbor Vow Studio — Business Card</title>
<link rel="stylesheet" href="https://fonts.googleapis.com/css2?family=Lato:wght@400;700&family=Montserrat:wght@600&display=swap">
<style>
  :root {
    --stage: #2b2b2b;
    --card-dark: #161616;
    --card-mid: #252525;
    --gold: #e2bf80;
    --gold-edge: #d9b36c;
    --blue: #58aa9e;
    --ink-light: #f4f4f2;
    --rule: #cfcfcf;
  }
  * { box-sizing: border-box; margin: 0; padding: 0; }
  html, body {
    width: 1200px;
    height: 900px;
    overflow: hidden;
    background: var(--stage);
    font-family: "Lato", sans-serif;
  }
  .stage {
    width: 1200px;
    height: 900px;
    display: flex;
    flex-direction: column;
    align-items: center;
    justify-content: center;
    gap: 44px;
  }
  .card {
    position: relative;
    width: 640px;
    height: 366px;
    background: linear-gradient(135deg, var(--card-dark) 0%, var(--card-mid) 60%, #1c1c1c 100%);
    border-bottom: 7px solid var(--gold-edge);
    box-shadow: 0 18px 40px rgba(0,0,0,0.45);
    color: var(--ink-light);
  }
  .brand-name {
    font-family: "Lato", sans-serif;
    font-weight: 400;
    color: var(--ink-light);
    letter-spacing: 0.04em;
    line-height: 1.2;
  }

  /* front */
  .card-front {
    display: flex;
    flex-direction: column;
    align-items: center;
    justify-content: center;
    padding-bottom: 20px;
  }
  .card-front .brand-name {
    font-size: 40px;
    text-align: center;
  }
  .brand-line {
    display: flex;
    align-items: center;
    gap: 14px;
  }
  .brand-dot {
    width: 14px;
    height: 14px;
    border-radius: 50%;
    background: var(--blue);
    flex: none;
  }
  .front-links {
    margin-top: 18px;
    text-align: center;
    font-size: 14px;
    letter-spacing: 0.22em;
    line-height: 1.7;
  }
  .front-web { color: var(--ink-light); }
  .front-handle { color: var(--blue); font-weight: 700; }

  /* back */
  .card-back {
    display: flex;
    align-items: center;
    padding: 0 36px 0 44px;
  }
  .card-back .brand-block {
    width: 220px;
    text-align: center;
  }
  .card-back .brand-name {
    font-size: 30px;
  }
  .brand-rule {
    width: 40px;
    height: 2px;
    background: var(--blue);
    margin: 12px auto 0;
  }
  .divider {
    width: 1px;
    height: 150px;
    background: var(--rule);
    margin: 0 26px 0 28px;
  }
  .contact-block { flex: 1; min-width: 0; }
  .person-name {
    font-family: "Montserrat", sans-serif;
    font-weight: 600;
    font-size: 26px;
    color: var(--gold);
    letter-spacing: 0.01em;
    line-height: 1.1;
  }
  .person-role {
    font-size: 17px;
    letter-spacing: 0.06em;
    margin-top: 3px;
  }
  .accent-dash {
    width: 14px;
    height: 2px;
    background: var(--blue);
    margin: 10px 0 10px;
  }
  .contact-list { list-style: none; }
  .contact-item {
    display: flex;
    align-items: center;
    gap: 10px;
    font-size: 16px;
    line-height: 1.5;
    letter-spacing: 0.02em;
    white-space: nowrap;
  }
  .contact-icon {
    width: 12px;
    height: 12px;
    flex: none;
  }
</style>
</head>
<body>
<main class="stage">
  <section class="card card-front" aria-label="Card front">
    <div class="brand-line">
      <span class="brand-dot" aria-hidden="true"></span>
      <p class="brand-name">Luma Harbor Vow Studio</p>
    </div>
    <div class="front-links">
      <p class="front-web">www.lumaharborvowstudio.com</p>
      <p class="front-handle">@sayidoatluma</p>
    </div>
  </section>

  <section class="card card-back" aria-label="Card back">
    <div class="brand-block">
      <p class="brand-name">Luma Harbor<br>Vow Studio</p>
      <div class="brand-rule" aria-hidden="true"></div>
    </div>
    <div class="divider"></div>
    <div class="contact-block">
      <h1 class="person-name">DELIA BRENNAN</h1>
      <p class="person-role">Owner &amp; Officiant</p>
      <div class="accent-dash"></div>
      <ul class="contact-list">
        <li class="contact-item">
          <svg class="contact-icon" viewBox="0 0 24 24" aria-hidden="true"><path fill="#58aa9e" d="M12 2a7 7 0 0 0-7 7c0 5 7 13 7 13s7-8 7-13a7 7 0 0 0-7-7zm0 9.5A2.5 2.5 0 1 1 12 6.5a2.5 2.5 0 0 1 0 5z"/></svg>
          <span>Isabela, Puerto Rico</span>
        </li>
        <li class="contact-item">
          <svg class="contact-icon" viewBox="0 0 24 24" aria-hidden="true"><path fill="#e2bf80" d="M6.6 10.8a15.1 15.1 0 0 0 6.6 6.6l2.2-2.2a1 1 0 0 1 1-.25 11.4 11.4 0 0 0 3.6.57 1 1 0 0 1 1 1V20a1 1 0 0 1-1 1A17 17 0 0 1 3 4a1 1 0 0 1 1-1h3.5a1 1 0 0 1 1 1c0 1.25.2 2.45.57 3.57a1 1 0 0 1-.25 1z"/></svg>
          <span>555.014.2871</span>
        </li>
        <li class="contact-item">
          <svg class="contact-icon" viewBox="0 0 24 24" aria-hidden="true"><rect x="2" y="5" width="20" height="14" fill="none" stroke="#e2bf80" stroke-width="2"/><polyline points="2,5 12,13 22,5" fill="none" stroke="#e2bf80" stroke-width="2"/></svg>
          <span>delia@lumaharborvowstudio.com</span>
        </li>
        <li class="contact-item">
          <svg class="contact-icon" viewBox="0 0 24 24" aria-hidden="true"><circle cx="12" cy="12" r="10" fill="#e2bf80"/><path d="M2 12h20M12 2c3 3 3 17 0 20M12 2c-3 3-3 17 0 20" fill="none" stroke="#1c1c1c" stroke-width="1.5"/></svg>
          <span>www.lumaharborvowstudio.com</span>
        </li>
      </ul>
    </div>
  </section>
</main>
</body>
</html>
```